Surgery Office Letterhead Design

I'm seeking new letterhead that will comprise all of our office locations and logo and other applicable information, per the following:

Office Locations:

Lakemont Institute for Jaw & Face Surgery at Cleburne
347 Hazelpine Court
Cleburne, Texas 76033
Phone 817.382.4706
Fax 817.382.9034

Lakemont Institute for Jaw & Face Surgery at Stephenville
518 Willowgate Boulevard
Stephenville, Texas 76401
Phone 254.563.2781
Fax 254.563.2789

Lakemont Institute for Jaw & Face Surgery at Belton
739 West 9th Avenue
Belton, Texas 76513
Phone 254.871.4035
Fax 254.871.4042

Other Info to include:

www.lakemontjawface.com
hello@lakemontjawface.com

Industry/Entity Type

Medical

Font styles to use
Serif
Sans Serif

Requirements
Must have
• See Project Description

```html
<!DOCTYPE html>
<html lang="en">
<head>
<meta charset="utf-8">
<title>Lakemont Institute for Jaw &amp; Face Surgery — Letterhead</title>
<link href="https://fonts.googleapis.com/css2?family=Open+Sans:wght@400;600&display=swap" rel="stylesheet">
<style>
  :root {
    --band-blue: #4d6788;
    --navy: #253a5e;
    --footer-tint: #dde3ed;
    --paper: #ffffff;
    --watermark: #f5f5f5;
    --rule: #c9d2df;
  }
  * { margin: 0; padding: 0; box-sizing: border-box; }
  html, body { width: 849px; height: 1200px; overflow: hidden; background: var(--paper); }
  .letterhead {
    position: relative;
    width: 849px;
    height: 1200px;
    background: var(--paper);
    font-family: "Open Sans", Arial, sans-serif;
  }
  .header-band {
    position: absolute;
    left: 0; top: 54px;
    width: 849px; height: 62px;
    background: var(--band-blue);
  }
  .brand-plate {
    position: absolute;
    left: 304px; top: 54px;
    width: 238px; height: 26px;
    background: var(--paper);
    box-shadow: 0 3px 2px -1px rgba(20, 30, 50, 0.75);
  }
  .brand-name {
    position: absolute;
    left: 304px; top: 26px;
    width: 238px;
    text-align: center;
    color: var(--navy);
    font-weight: 600;
    font-size: 11.5px;
    line-height: 14px;
    letter-spacing: 0.6px;
  }
  .header-address {
    position: absolute;
    left: 0; top: 89px;
    width: 849px;
    text-align: center;
    color: var(--paper);
    font-size: 14.5px;
    letter-spacing: 1.45px;
    line-height: 20px;
  }
  .watermark-area {
    position: absolute;
    left: 250px; top: 342px;
    width: 348px; height: 516px;
    border-radius: 60px;
    background: radial-gradient(ellipse at center, var(--watermark) 0%, #fafafa 60%, var(--paper) 100%);
  }
  .office-list {
    position: absolute;
    left: 24px; top: 1076px;
    width: 801px;
    display: grid;
    grid-template-columns: repeat(3, 1fr);
    border-top: 1px solid var(--rule);
    padding-top: 10px;
    color: var(--navy);
    font-size: 10px;
    line-height: 14px;
    text-align: center;
  }
  .office + .office { border-left: 1px solid var(--rule); }
  .office-name { font-weight: 600; }
  .footer-band {
    position: absolute;
    left: 0; top: 1166px;
    width: 849px; height: 34px;
    background: var(--footer-tint);
    display: flex;
    justify-content: center;
    align-items: center;
    gap: 17px;
    color: var(--navy);
    font-size: 15px;
    letter-spacing: 0.3px;
  }
  .contact-item { display: flex; align-items: center; gap: 6px; }
  .contact-icon { width: 13px; height: 13px; fill: var(--navy); }
</style>
</head>
<body>
  <main class="letterhead">
    <div class="header-band"></div>
    <div class="brand-plate"></div>
    <div class="brand-name">LAKEMONT INSTITUTE<br>FOR JAW &amp; FACE SURGERY</div>
    <p class="header-address">347 Hazelpine Court, Cleburne, Texas 76033 | www.lakemontjawface.com</p>

    <div class="watermark-area" role="img" aria-label="Faint stethoscope illustration as a background watermark"></div>

    <section class="office-list" aria-label="Office locations">
      <address class="office">
        <div class="office-name">Lakemont Institute for Jaw &amp; Face Surgery<br>at Cleburne</div>
        347 Hazelpine Court, Cleburne, Texas 76033<br>
        Phone 817.382.4706 · Fax 817.382.9034
      </address>
      <address class="office">
        <div class="office-name">Lakemont Institute for Jaw &amp; Face Surgery<br>at Stephenville</div>
        518 Willowgate Boulevard, Stephenville, Texas 76401<br>
        Phone 254.563.2781 · Fax 254.563.2789
      </address>
      <address class="office">
        <div class="office-name">Lakemont Institute for Jaw &amp; Face Surgery<br>at Belton</div>
        739 West 9th Avenue, Belton, Texas 76513<br>
        Phone 254.871.4035 · Fax 254.871.4042
      </address>
    </section>

    <footer class="footer-band">
      <span class="contact-item">
        <svg class="contact-icon" viewBox="0 0 16 16" aria-hidden="true">
          <circle cx="8" cy="8" r="7.5"/>
          <path d="M4 5c2 0 2 2 4 2s1 3-1 3-1 3-3 2zM10 3c1 1 3 2 3 4-1 0-2-1-3-1z" fill="#dde3ed"/>
        </svg>
        hello@lakemontjawface.com
      </span>
      <span class="contact-item">
        <svg class="contact-icon" viewBox="0 0 16 16" aria-hidden="true">
          <path d="M3.5 1l2.6 3.2-1.5 1.7c.9 2 2.6 3.8 4.6 4.7l1.6-1.6L14 11.6 12.4 14.5C6.6 14 2 9.4 1.5 3.4z"/>
        </svg>
        817.382.4706
      </span>
      <span class="contact-item">
        <svg class="contact-icon" viewBox="0 0 16 16" aria-hidden="true">
          <rect x="1" y="5" width="3" height="10" rx="1"/>
          <path d="M5 4h3V1h5l2 2v12H5z"/>
          <g fill="#dde3ed">
            <rect x="7" y="7" width="6" height="2"/>
            <rect x="7" y="10" width="2" height="1.5"/>
            <rect x="10" y="10" width="2" height="1.5"/>
            <rect x="7" y="12.5" width="2" height="1.5"/>
            <rect x="10" y="12.5" width="2" height="1.5"/>
          </g>
        </svg>
        817.382.9034
      </span>
    </footer>
  </main>
</body>
</html>
```